Tolvane Global Wordpress website design

We need a worddpress website/theme design for a new outsourcing company based in Australia.Name of the company is "Tolvane".
Website content is in progress.
The design needs to be clean without clutter in any section. Some example websites are provided below
Menu
- Resources
- Services
- Our difference
Home page needs to have a gif image, for example http://www.brindleworks.example. or http://www.corvathicket.example or http://www.corvathicket.example/team.html
We like how the corvathicket website flows without having the need to click on the menu. It is also mobile friendly (which is important)
Each piece of content will have a learn more button
A call to action button will be placed on the home page, which will provide our phone number and access to online form*
A call to action button will also be added to various other pages such as Resources.
Resources Section will contain web articles, whitepapers, blog and any other ccontent which helps customer in making a decision
Having the ability to add a video or images on the home page is also important
Ability to edit the content easily via wordpress is extremely important
* This is a great Contact Us form - http://www.pelgrastudio.example/#/schedule-meeting
* We do not need the traditional web form on the contact us page
Target Market(s)
Small to medium businesses requiring outsourcing services
Industry/Entity Type
It Company
Coding
Coded - Design and coding required
Colors
Designer to choose colors to be used in the design.
Look and feel
Each slider illustrates characteristics of the customer's brand and the style your logo design should communicate.

```html
<!DOCTYPE html>
<html lang="en">
<head>
<meta charset="utf-8">
<title>Tolvane – Outsourcing</title>
<link href="https://fonts.googleapis.com/css2?family=Montserrat:wght@400;500;600;700&family=Open+Sans:wght@400;600;700&display=swap" rel="stylesheet">
<style>
:root{
  --red:#e8333a;
  --ink:#1f1f1f;
  --text:#6b6b6b;
  --line:#cfcfcf;
  --white:#ffffff;
  --footer:#232323;
  --footer-text:#d8d8d8;
  --ring:#e9c9cf;
}
*{box-sizing:border-box;margin:0;padding:0}
html,body{width:1200px;height:3285px;overflow:hidden}
body{position:relative;font-family:"Open Sans",sans-serif;color:var(--text);background:var(--white)}
.abs{position:absolute}
h1,h2,h3,h4,.nav,.brand{font-family:"Montserrat",sans-serif}

/* hero */
.hero{left:0;top:0;width:1200px;height:537px;background:linear-gradient(180deg,#56667a 0%,#8c8f93 35%,#b5976c 52%,#4b5868 70%,#2d3a4a 100%)}
.topbar-phone{right:90px;top:18px;color:var(--white);font-size:15px;font-weight:700;display:flex;align-items:center;gap:8px}
.brand{color:var(--white);letter-spacing:7px;font-weight:500}
.header-brand{left:97px;top:50px;font-size:40px}
.nav{right:90px;top:60px;display:flex;gap:34px;font-size:14px;font-weight:600;color:var(--white);text-transform:uppercase;align-items:center}
.nav .active{color:var(--red)}
.hero-title{left:97px;top:188px;font-size:68px;letter-spacing:12px;color:var(--white);font-weight:500}
.hero-sub{left:99px;top:276px;font-size:25px;line-height:36px;color:var(--white);font-weight:600;width:460px}
.cta{left:99px;top:371px;height:46px;width:300px;background:var(--red);color:var(--white);font-size:15px;font-weight:700;display:flex;align-items:center;padding-left:46px;letter-spacing:.4px}
.cta svg{position:absolute;left:4px;top:4px}
.bubble{background:var(--white);color:#555;font-size:13px;line-height:19px;padding:9px 14px;border-radius:2px}
.bubble.red{background:var(--red);color:var(--white)}
.bubble::before{content:"";position:absolute;left:-14px;top:16px;border:8px solid transparent;border-right-color:inherit}
.b1{left:710px;top:178px;width:298px}
.b1::before{border-right-color:var(--red)}
.b2{left:710px;top:272px;width:350px}
.b2::before{border-right-color:var(--white)}
.b3{left:710px;top:385px;width:214px}
.b3::before{border-right-color:var(--white)}
.scroll-btn{width:100px;height:100px;border-radius:50%;background:#8d8d8d;display:flex;align-items:center;justify-content:center}
.scroll-btn span{width:64px;height:64px;border-radius:50%;background:var(--white);display:flex;align-items:center;justify-content:center}

/* welcome */
.section-title{width:1200px;text-align:center;font-size:32px;font-weight:600;color:var(--ink);letter-spacing:.5px}
.intro{left:200px;width:800px;text-align:center;font-size:13.5px;line-height:28px}
.card{width:424px;height:160px;border:1.5px solid var(--line);background:var(--white);padding:24px 28px}
.card h3{font-size:20px;font-weight:600;color:var(--ink);margin-bottom:14px;letter-spacing:.4px}
.card p{font-size:13.5px;line-height:24px}
.card .more{display:block;margin-top:12px;font-size:12.5px;font-weight:700;color:var(--red)}
.card.left{text-align:right;padding-right:80px}
.card.right{text-align:left;padding-left:66px}
.icon-ring{width:96px;height:96px;border-radius:50%;border:1.5px solid var(--line);background:var(--white);display:flex;align-items:center;justify-content:center}

/* video */
.video{left:0;top:1275px;width:1200px;height:466px;background:linear-gradient(160deg,#cfc9c2 0%,#8e8a85 35%,#3e4453 65%,#2a2c33 100%)}
.play{left:563px;top:1472px;width:74px;height:74px;border-radius:50%;background:rgba(40,40,40,.55);border:3px solid rgba(255,255,255,.85);display:flex;align-items:center;justify-content:center}

/* resources */
.post{width:308px}
.post .thumb{width:308px;height:217px}
.post h4{margin-top:44px;font-size:18.5px;font-weight:700;color:var(--ink);letter-spacing:.3px}
.post .meta{margin-top:10px;font-size:12.5px;display:flex;gap:16px;align-items:center}
.post .meta span{display:flex;align-items:center;gap:6px}
.post p{margin-top:12px;font-size:13.5px;line-height:25px}
.post .more{display:block;margin-top:14px;font-size:12.5px;font-weight:700;color:var(--red)}

/* difference */
.difference{left:0;top:2424px;width:1200px;height:467px;background:linear-gradient(110deg,#6f6459 0%,#b9aea3 40%,#d8d5d2 60%,#cab9b5 100%)}
.diff-title{left:97px;top:2530px;font-size:50px;line-height:60px;color:var(--white);font-weight:600;letter-spacing:1px}
.diff-text{left:99px;top:2648px;width:390px;font-size:13.5px;line-height:26px;color:var(--white)}
.ghost{left:99px;top:2751px;width:138px;height:44px;border:1.5px solid var(--white);color:var(--white);font-size:13px;font-weight:700;display:flex;align-items:center;padding-left:40px}
.ghost svg{position:absolute;left:2px;top:2px}

/* footer */
.footer{left:0;top:2891px;width:1200px;height:394px;background:var(--footer)}
.foot-brand{left:97px;top:3073px;font-size:42px}
.foot-h{font-size:16px;font-weight:600;color:var(--white);letter-spacing:.4px}
.quick{left:407px;top:3040px;list-style:none;font-size:12.5px;color:var(--footer-text);line-height:30px}
.news-text{left:593px;top:3040px;width:270px;font-size:12.5px;line-height:22px;color:var(--footer-text)}
.field{left:593px;top:3093px;width:252px;height:36px;background:var(--white);color:#777;font-size:12.5px;padding:10px 12px}
.subscribe{left:593px;top:3144px;width:100px;height:32px;border:1.5px solid #bbb;color:var(--white);font-size:12px;font-weight:600;display:flex;align-items:center;justify-content:center}
.contact{left:915px;font-size:12.5px;line-height:21px;color:var(--footer-text);display:flex;gap:16px}
.divider{left:99px;top:3212px;width:1000px;height:1px;background:#3e3e3e}
.copy{left:99px;top:3240px;font-size:12.5px;color:var(--footer-text)}
.social{left:975px;top:3235px;display:flex;gap:8px}
.social span{width:28px;height:28px;border-radius:50%;border:1.5px solid #bbb;display:block}
</style>
</head>
<body>

<!-- Hero -->
<section class="abs hero" role="img" aria-label="Evening harbour city skyline with boats on the water"></section>
<div class="abs topbar-phone">
  <svg width="14" height="14" viewBox="0 0 24 24"><path fill="#e8333a" d="M6.6 10.8a15 15 0 006.6 6.6l2.2-2.2a1 1 0 011-.25 11.4 11.4 0 003.6.57 1 1 0 011 1V20a1 1 0 01-1 1A17 17 0 013 4a1 1 0 011-1h3.5a1 1 0 011 1 11.4 11.4 0 00.57 3.6 1 1 0 01-.25 1z"/></svg>
  1 800 555 0142
</div>
<div class="abs brand header-brand">TOLVANE</div>
<nav class="abs nav">
  <span class="active">Home</span><span>Resources</span><span>Services</span><span>Our Difference</span><span>Contact Us</span>
  <svg width="15" height="15" viewBox="0 0 24 24"><circle cx="10" cy="10" r="7" fill="none" stroke="#fff" stroke-width="3"/><path d="M15 15l6 6" stroke="#fff" stroke-width="3"/></svg>
</nav>
<h1 class="abs hero-title">TOLVANE</h1>
<p class="abs hero-sub">We are a new outsourcing company based in Australia</p>
<div class="abs cta">
  <svg width="36" height="38" viewBox="0 0 36 38"><path d="M4 4l14 15L4 34M16 4l14 15-14 15" fill="none" stroke="#fff" stroke-width="3"/></svg>
  REQUEST FREE CONSULTATION
</div>
<div class="abs bubble red b1">At vero eos et accusamus et iusto odio dignissimos ducimus qui</div>
<div class="abs bubble b2">Nam libero tempore, cum soluta nobis est egendi optio cumque nihil impedit quo minus id quomax ime placeat facere possimus, omnis.</div>
<div class="abs bubble b3">Asamus et iusto odio dignis simos ducimus qui</div>
<div class="abs scroll-btn" style="left:550px;top:487px"><span>
  <svg width="34" height="30" viewBox="0 0 34 30"><path d="M4 4l13 11L30 4M4 14l13 11 13-11" fill="none" stroke="#555" stroke-width="3"/></svg>
</span></div>

<!-- Welcome -->
<h2 class="abs section-title" style="left:0;top:646px">WELCOME TO TOLVANE</h2>
<p class="abs intro" style="top:714px">Nam libero tempore, cum soluta nobis est eligendi optio cumque nihil impedit quo minus id quod maxime placeat facere possimus, omnis voluptas assumenda est, omnis dolor repellendu bus autem quibusdam et aut officiis</p>

<div class="abs card left" style="left:99px;top:821px"><h3>MAINTENANCE</h3><p>At vero eos et accusamus et iusto odio dignissimos uos dolores et quas molestias excep</p><span class="more">LEARN MORE &gt;&gt;</span></div>
<div class="abs icon-ring" style="left:486px;top:853px"><svg width="34" height="34" viewBox="0 0 24 24"><path fill="#e8333a" d="M22.7 19l-9.1-9.1a6 6 0 00-7.9-7.6l3.9 3.9-2.8 2.8-4-3.9a6 6 0 007.6 7.9l9.1 9.1a1 1 0 001.4 0l1.8-1.8a1 1 0 000-1.3z"/></svg></div>

<div class="abs card right" style="left:675px;top:821px"><h3>MODERNIZATION</h3><p>At vero eos et accusamus et iusto odio dignissimos uos dolores et quas molestias excep</p><span class="more">LEARN MORE &gt;&gt;</span></div>
<div class="abs icon-ring" style="left:627px;top:853px"><svg width="30" height="34" viewBox="0 0 20 24"><path fill="#e8333a" d="M2 0h11l7 7v17H2z"/><path d="M13 0v7h7" fill="#f49aa0"/><path d="M5 12h10M5 16h10M5 20h7" stroke="#fff" stroke-width="1.6"/></svg></div>

<div class="abs card left" style="left:99px;top:1012px"><h3>DEVELOPMENT</h3><p>At vero eos et accusamus et iusto odio dignissimos uos dolores et quas molestias excep</p><span class="more">LEARN MORE &gt;&gt;</span></div>
<div class="abs icon-ring" style="left:486px;top:1044px"><svg width="38" height="34" viewBox="0 0 38 34"><circle cx="14" cy="18" r="8" fill="none" stroke="#e8333a" stroke-width="6" stroke-dasharray="3 2.3"/><circle cx="14" cy="18" r="3" fill="#e8333a"/><circle cx="29" cy="9" r="5" fill="none" stroke="#e8333a" stroke-width="4" stroke-dasharray="2 1.7"/><circle cx="29" cy="26" r="4" fill="none" stroke="#e8333a" stroke-width="3.5" stroke-dasharray="2 1.6"/></svg></div>

<div class="abs card right" style="left:675px;top:1012px"><h3>INTEGRATION</h3><p>At vero eos et accusamus et iusto odio dignissimos uos dolores et quas molestias excep</p><span class="more">LEARN MORE &gt;&gt;</span></div>
<div class="abs icon-ring" style="left:627px;top:1044px"><svg width="34" height="28" viewBox="0 0 34 28"><path d="M2 8h26M22 2l7 6-7 6M32 20H6M12 14l-7 6 7 6" fill="none" stroke="#e8333a" stroke-width="3.5"/></svg></div>

<!-- Video -->
<section class="abs video" role="img" aria-label="Video still of business partners shaking hands across a meeting table"></section>
<div class="abs play"><svg width="26" height="28" viewBox="0 0 26 28"><path d="M4 2l20 12L4 26z" fill="#fff"/></svg></div>

<!-- Resources -->
<h2 class="abs section-title" style="left:0;top:1826px">RESOURCES</h2>

<article class="abs post" style="left:99px;top:1907px">
  <div class="thumb" role="img" aria-label="Team reviewing printed charts with coffee on a desk" style="background:linear-gradient(135deg,#5b4c40,#c9c2b8 60%,#8a7a6a)"></div>
  <h4>FINIBUS BONORUM ET MALO</h4>
  <div class="meta"><span><svg width="11" height="11" viewBox="0 0 12 12"><rect x="1" y="2" width="10" height="9" fill="#e8333a"/></svg>16/08/2017</span><span><svg width="11" height="11" viewBox="0 0 12 12"><circle cx="6" cy="3.5" r="2.5" fill="#e8333a"/><path d="M1 12a5 5 0 0110 0z" fill="#e8333a"/></svg>John Doe</span></div>
  <p>Nam libero tempore, cum soluta nobis est elige ndi optio cumque nihil impedit quo minus id qu od maxime placeat facere pos.</p>
  <span class="more">LEARN MORE &gt;&gt;</span>
</article>
<article class="abs post" style="left:445px;top:1907px">
  <div class="thumb" role="img" aria-label="Hand touching a glowing world network display" style="background:linear-gradient(135deg,#1c2a52,#3d64b8 55%,#9aa6c0)"></div>
  <h4>FINIBUS BONORUM ET MALO</h4>
  <div class="meta"><span><svg width="11" height="11" viewBox="0 0 12 12"><rect x="1" y="2" width="10" height="9" fill="#e8333a"/></svg>16/08/2017</span><span><svg width="11" height="11" viewBox="0 0 12 12"><circle cx="6" cy="3.5" r="2.5" fill="#e8333a"/><path d="M1 12a5 5 0 0110 0z" fill="#e8333a"/></svg>John Doe</span></div>
  <p>Nam libero tempore, cum soluta nobis est elige ndi optio cumque nihil impedit quo minus id qu od maxime placeat facere pos.</p>
  <span class="more">LEARN MORE &gt;&gt;</span>
</article>
<article class="abs post" style="left:791px;top:1907px">
  <div class="thumb" role="img" aria-label="Desk with sketched outsourcing concept notes" style="background:linear-gradient(135deg,#d9d4cc,#f2efea 50%,#c8b9a8)"></div>
  <h4>FINIBUS BONORUM ET MALO</h4>
  <div class="meta"><span><svg width="11" height="11" viewBox="0 0 12 12"><rect x="1" y="2" width="10" height="9" fill="#e8333a"/></svg>16/08/2017</span><span><svg width="11" height="11" viewBox="0 0 12 12"><circle cx="6" cy="3.5" r="2.5" fill="#e8333a"/><path d="M1 12a5 5 0 0110 0z" fill="#e8333a"/></svg>John Doe</span></div>
  <p>Nam libero tempore, cum soluta nobis est elige ndi optio cumque nihil impedit quo minus id qu od maxime placeat facere pos.</p>
  <span class="more">LEARN MORE &gt;&gt;</span>
</article>

<!-- Our difference -->
<section class="abs difference" role="img" aria-label="Hand drawing a network diagram of connected points"></section>
<h2 class="abs diff-title">OUR<br>DIFFERENCE</h2>
<p class="abs diff-text">Nam libero tempore, cum soluta nobis est eligendi optio cumque nihil impedit quo minus id quod maxime placeat facere possimus, omnis voluptas as...</p>
<div class="abs ghost">
  <svg width="34" height="38" viewBox="0 0 34 38"><path d="M4 4l13 15L4 34M14 4l13 15-13 15" fill="none" stroke="#fff" stroke-width="2.5"/></svg>
  LEARN MORE
</div>

<!-- Footer -->
<footer class="abs footer"></footer>
<div class="abs scroll-btn" style="left:552px;top:2841px;background:#1a1a1a"><span>
  <svg width="30" height="20" viewBox="0 0 30 20"><path d="M3 17L15 5l12 12" fill="none" stroke="#222" stroke-width="4"/></svg>
</span></div>
<div class="abs brand foot-brand">TOLVANE</div>

<h4 class="abs foot-h" style="left:407px;top:2998px">QUICK LINKS</h4>
<ul class="abs quick"><li>Home,</li><li>Resources</li><li>Services</li><li>Our Difference</li><li>Contact us</li></ul>

<h4 class="abs foot-h" style="left:593px;top:2998px">NEWSLETTER SUBSCRIPTION</h4>
<p class="abs news-text">Register your Email Address to get Information about us</p>
<div class="abs field">Email Address</div>
<div class="abs subscribe">SUBSCRIBE</div>

<h4 class="abs foot-h" style="left:915px;top:2998px">CONTACT US</h4>
<div class="abs contact" style="top:3040px"><svg width="12" height="16" viewBox="0 0 12 16"><path d="M6 0a6 6 0 016 6c0 4-6 10-6 10S0 10 0 6a6 6 0 016-6z" fill="#fff"/><circle cx="6" cy="6" r="2" fill="#232323"/></svg><span>4720 Harbourline Road Suite 310<br>Port Avenna, QL 4102</span></div>
<div class="abs contact" style="top:3104px"><svg width="13" height="13" viewBox="0 0 24 24"><path fill="#fff" d="M6.6 10.8a15 15 0 006.6 6.6l2.2-2.2a1 1 0 011-.25 11.4 11.4 0 003.6.57 1 1 0 011 1V20a1 1 0 01-1 1A17 17 0 013 4a1 1 0 011-1h3.5a1 1 0 011 1 11.4 11.4 0 00.57 3.6 1 1 0 01-.25 1z"/></svg><span>1 800 555 0142</span></div>
<div class="abs contact" style="top:3147px"><svg width="14" height="12" viewBox="0 0 14 12"><rect width="14" height="12" fill="#fff"/><path d="M0 1l7 5 7-5" fill="none" stroke="#232323" stroke-width="1.4"/></svg><span>info@tolvane.example</span></div>

<div class="abs divider"></div>
<p class="abs copy">Copyrights © 2017, Tolvane.&nbsp; All rights reserved.</p>
<div class="abs social" aria-label="Social links"><span></span><span></span><span></span><span></span></div>

</body>
</html>
```